Coral Bend Tallow Creek Seniors Fairway Festival 2107

I would like a design for an A4 Event Flyer.

This is a golf event for Senior ladies and gentlemen. I would like the design to appeal to an older age group.

I would like somewhere on the flyer a golf ball image with the following details inside "Please put me on your notice board"

The information on the Flyer is as follows
- (Title - Coral bend Tallow Creek Seniors Fairway Festival 2017)
- Date 16th of October to 20th of October
- Over 55 years of age
- We invite our fellow Veteran Ladies and Gentlemen to play a unique 54 hole stableford event at three fantastic Golf Courses, and finish the week at Bramwick Golf club with a 2BBB Medley.
- Insert schedule that is attached in PDF. They layout can be changed.

- For entry form and details
Contact: Bramwick Proshop on 02 61938842 or email admin@bramwickelmsidelinks.example.au

I have attached 4 golf course images. This is a photo of each course. Could I please get these added to the flyer.

Target Market(s)

seniors

Industry/Entity Type

Golf Course

Requirements
Must have
• All information provided

```html
<!DOCTYPE html>
<html lang="en">
<head>
<meta charset="utf-8">
<title>Coral Bend Tallow Creek Seniors Fairway Festival 2017 – Event Flyer</title>
<link href="https://fonts.googleapis.com/css2?family=Open+Sans:wght@400;600;700;800&display=swap" rel="stylesheet">
<style>
  :root{
    --page-bg:#e4e4e4;
    --green:#1f6b2e;
    --green-dark:#155223;
    --navy:#23407a;
    --sky-top:#2a6fd0;
    --sky-low:#cfe3f7;
    --gold-light:#f6d9a6;
    --gold:#d9a25a;
    --gold-dark:#b47a2e;
    --ink:#222;
    --muted:#666;
    --table-bg:#ededed;
    --rule:#9a9a9a;
    --white:#fff;
  }
  *{box-sizing:border-box;margin:0;padding:0}
  html,body{width:1200px;height:800px;overflow:hidden}
  body{background:var(--page-bg);font-family:"Open Sans",Arial,sans-serif;color:var(--ink);position:relative}

  .flyer{position:absolute;left:331px;top:20px;width:537px;height:760px;background:var(--white);overflow:hidden;box-shadow:0 4px 18px rgba(0,0,0,.18)}

  /* header */
  .hero-photo{position:absolute;left:0;top:0;width:537px;height:236px;
    background:linear-gradient(180deg,var(--sky-top) 0%,#5d98de 45%,var(--sky-low) 100%)}
  .event-title{position:absolute;right:22px;top:44px;width:230px;text-align:right;color:var(--white)}
  .event-title .kicker{font-size:22px;font-weight:600;letter-spacing:1px;line-height:1}
  .event-title .name{font-size:18px;font-weight:700;line-height:1.3}
  .event-title .year{font-size:40px;font-weight:400;line-height:1.05}
  .region{position:absolute;right:22px;top:150px;text-align:right;color:var(--navy);font-weight:800;font-size:17px;line-height:1.3;letter-spacing:.3px}

  .date-pill{position:absolute;right:0;top:208px;width:250px;height:36px;border-radius:18px 0 0 18px;
    background:linear-gradient(180deg,var(--gold-light),var(--gold));color:var(--navy);
    font-size:15px;font-weight:600;display:flex;align-items:center;padding-left:18px;box-shadow:0 2px 3px rgba(0,0,0,.15)}
  .date-pill sup{font-size:9px}
  .age-note{position:absolute;right:18px;top:250px;color:var(--green);font-size:12px;font-weight:600}

  .intro{position:absolute;left:20px;top:246px;width:262px;font-size:10.5px;line-height:1.35;color:var(--ink)}

  /* schedule */
  .schedule{position:absolute;left:20px;top:312px;width:497px;height:196px;background:var(--table-bg);display:flex}
  .schedule-heading{width:56px;background:var(--white);margin:8px 0;display:flex;align-items:center;justify-content:center}
  .schedule-heading h2{writing-mode:vertical-rl;transform:rotate(180deg);color:var(--green);font-size:10.5px;font-weight:700;line-height:1.25;text-align:center}
  .schedule-table{flex:1;border-collapse:collapse;margin:6px 12px;font-size:10.5px}
  .schedule-table td{border-bottom:1px solid var(--rule);padding:3px 2px;vertical-align:top;color:var(--ink)}
  .schedule-table tr:last-child td{border-bottom:none}
  .schedule-table .day{color:var(--green);font-weight:600;width:95px;font-size:11px}
  .schedule-table .date{color:var(--green);width:78px}
  .schedule-table .venue{color:var(--green)}
  .schedule-table .note{display:block;color:var(--muted);font-size:9.5px;font-weight:400}

  /* lower photo area */
  .ball-photo{position:absolute;left:0;top:512px;width:537px;height:210px;
    background:radial-gradient(circle at 78% 40%,#f2f6fb 0 12%,transparent 13%),
               linear-gradient(180deg,#2a1d10 0%,#5a4a25 55%,#6e8a2e 100%)}
  .course-grid{position:absolute;left:22px;top:522px;width:278px;display:grid;grid-template-columns:136px 130px;gap:8px 12px}
  .course-photo{height:76px;border:2px solid var(--white);
    background:linear-gradient(180deg,#8dbbe6 0%,#5f8f3c 45%,#4e8a2c 100%)}
  .course-photo.alt{background:linear-gradient(180deg,#6a9a45 0%,#4a8030 60%,#3c6d25 100%)}

  /* footer */
  .web-band{position:absolute;left:0;top:690px;width:537px;height:70px}
  .web-address{position:absolute;left:14px;top:697px;color:var(--green);font-size:15px;font-weight:700}
  .contact{position:absolute;left:14px;top:721px;color:var(--white);font-size:11px;line-height:1.45}
  .contact strong{font-weight:600;font-size:12px}
  .contact .label{opacity:.85}

  .notice-badge{position:absolute;right:10px;top:640px;width:112px;height:112px;border-radius:50%;
    background:radial-gradient(circle at 35% 30%,var(--gold-light),var(--gold) 60%,var(--gold-dark));
    border:3px solid var(--white);color:var(--white);font-size:12.5px;line-height:1.2;font-weight:600;
    display:flex;align-items:center;justify-content:center;text-align:center;text-shadow:0 1px 1px rgba(0,0,0,.25)}
</style>
</head>
<body>
  <article class="flyer">
    <div class="hero-photo" role="img" aria-label="Photo of a smiling senior couple holding golf clubs under palm trees and blue sky"></div>

    <div class="event-title">
      <div class="kicker">SENIORS</div>
      <div class="name">Fairway Festival</div>
      <div class="year">2017</div>
    </div>
    <div class="region">CORAL BEND<br>TALLOW CREEK</div>

    <div class="date-pill">16<sup>th</sup>&nbsp;October to 20<sup>th</sup>&nbsp;October</div>
    <div class="age-note">Over 55 years of age</div>

    <p class="intro">We invite our fellow Veteran Ladies and Gentlemen to play a unique 54 hole stableford event at three fantastic Golf Courses, and finish the week at Bramwick Golf club with a 2BBB Medley.</p>

    <section class="schedule">
      <div class="schedule-heading">
        <h2>CORAL BEND / TALLOW CREEK<br>SENIORS' FAIRWAY FESTIVAL<br>PROGRAM</h2>
      </div>
      <table class="schedule-table">
        <tr><td class="day">Sunday</td><td class="date">15 October</td><td class="venue">Bramwick Golf Club<span class="note">Registrations: 4.00pm - 6.00pm</span></td></tr>
        <tr><td class="day">Monday</td><td class="date">16 October</td><td class="venue">Harlow Point Golf Course Par 72<span class="note">Stableford - 1st Round Championships</span></td></tr>
        <tr><td class="day">Tuesday<span class="note">CTSGA Trophy Day</span></td><td class="date">17 October</td><td class="venue">Millbrook Golf Course Par 71<span class="note">Stableford - 2nd Round Championships</span></td></tr>
        <tr><td class="day">Wednesday</td><td class="date">18 October</td><td class="venue">LEISURE</td></tr>
        <tr><td class="day">Thursday</td><td class="date">19 October</td><td class="venue">Ridgewater Golf Course Par 72<span class="note">Stableford - Round 3 Championships</span></td></tr>
        <tr><td class="day">Friday</td><td class="date">20 October</td><td class="venue">Bramwick Golf Course Par 66<span class="note">18 Hole 2BBB Medley Stableford</span></td></tr>
      </table>
    </section>

    <div class="ball-photo" role="img" aria-label="Close-up photo of a golf ball on a tee against a blurred green course"></div>
    <div class="course-grid">
      <div class="course-photo" role="img" aria-label="Golf course photo one: fairway with bunker and trees"></div>
      <div class="course-photo" role="img" aria-label="Golf course photo two: open fairway with hills behind"></div>
      <div class="course-photo" role="img" aria-label="Golf course photo three: green framed by tall trees"></div>
      <div class="course-photo alt" role="img" aria-label="Golf course photo four: green with sand trap"></div>
    </div>

    <svg class="web-band" viewBox="0 0 537 70" aria-hidden="true">
      <path d="M0 10 Q200 0 537 -6 L537 70 L0 70 Z" fill="#ffffff"/>
      <path d="M0 28 Q220 22 537 14 L537 70 L0 70 Z" fill="#1f6b2e"/>
    </svg>
    <div class="web-address">www.bramwickelmsidelinks.example.au</div>
    <div class="contact">
      For entry form and details contact <strong>Bramwick Proshop</strong><br>
      <span class="label">Ph:</span> 02 61938842 &nbsp;|&nbsp; <span class="label">Mail:</span> admin@bramwickelmsidelinks.example.au
    </div>

    <div class="notice-badge">Please<br>put me on your<br>notice board</div>
  </article>
</body>
</html>
```